Fotograf sucht Gutschein-Design
Zielgruppe
Bin Fotograf spezialisiert auf Pärchen und Hochzeitsfotos
Aufgabenstellung
Möchte einen neuen Gutschein für meine Zwecke haben. Sollte zu meinem fotografischen Stil passen, hell/ freundlich/ Retro? Vintage? Kann auch gerne 'Verzierung' mit Blümchen/ Zweige enthalten wenns passt. am besten ein wenig auf meiner Homepage orientieren >>> www.jonaskeltermann.com - Auch meine Logo/ Firmendaten sollten wo passend platziert sein. Mein Logo/ und Fotos füge ich bei und können wie es gut passt verwendet werden. Das auf dem Einzelbild bin ich, falls es wo passt wäre es toll. Schriftmäßig sollte es natürlich irgendwie das Wort Gutschein enthalten. Dann noch 'von' und 'für' und ein Feld wo ich händisch die Gutscheinnummer eintragen kann. Das Format/ Form überlasse ich auch ganz euch aber werde voraussichtlich bei blattkurier bestellen. (Falls es um das finden des passenden Formats/ Form geht). Bei Fragen könnt ihr euch gerne jederzeit melden.

```html
<!DOCTYPE html>
<html lang="de">
<head>
<meta charset="utf-8">
<title>Gutschein – Jonas Keltermann Fotografie</title>
<link href="https://fonts.googleapis.com/css2?family=Quicksand:wght@300;400;500&display=swap" rel="stylesheet">
<style>
  :root {
    --paper: #ffffff;
    --frame: #6f6f6f;
    --ink: #161616;
    --panel-warm: #eadfa8;
    --panel-cool: #f0efed;
    --logo-tile: #efefef;
    --leaf: #d8c9a8;
  }
  * { margin: 0; padding: 0; box-sizing: border-box; }
  html, body { width: 1200px; height: 446px; overflow: hidden; background: var(--paper); }
  body { font-family: "Quicksand", sans-serif; color: var(--ink); position: relative; }

  .voucher-frame {
    position: absolute; left: 40px; top: 16px; width: 1122px; height: 401px;
    border: 1px solid var(--frame);
  }
  .voucher-panel {
    position: absolute; left: 58px; top: 34px; width: 567px; height: 365px;
    background: linear-gradient(90deg, var(--panel-warm) 0%, #ece6c8 45%, var(--panel-cool) 100%);
  }
  .voucher-title {
    position: absolute; left: 82px; top: 52px;
    font-weight: 300; font-size: 120px; line-height: 1; letter-spacing: 1px;
  }
  .voucher-field {
    position: absolute; left: 90px; font-size: 20px; font-weight: 400; line-height: 1;
  }
  .voucher-line {
    position: absolute; height: 0; border-top: 1.5px solid var(--ink);
  }

  .brand-tile {
    position: absolute; left: 635px; top: 34px; width: 143px; height: 158px;
    background: var(--logo-tile);
    display: flex; flex-direction: column; align-items: center; justify-content: center; gap: 6px;
    font-weight: 400; font-size: 11px; letter-spacing: 2px; text-transform: uppercase; text-align: center;
  }
  .brand-mark { width: 34px; height: 34px; border-radius: 50%; border: 1.5px solid var(--ink); margin-bottom: 10px; }

  .photo { position: absolute; }
  .leaf-spray { position: absolute; border-radius: 50%; opacity: .55; }
</style>
</head>
<body>
  <div class="voucher-frame"></div>
  <div class="voucher-panel"></div>

  <div class="leaf-spray" role="img" aria-label="Zarter Zweig als Verzierung" style="left:26px;top:8px;width:140px;height:138px;background:radial-gradient(ellipse at center, var(--leaf) 0%, rgba(216,201,168,0) 70%);"></div>

  <h1 class="voucher-title">Gutschein</h1>

  <div class="voucher-field" style="top:246px;">Betrag:</div>
  <div class="voucher-line" style="left:176px;top:263px;width:170px;"></div>
  <div class="voucher-field" style="top:275px;">von:</div>
  <div class="voucher-line" style="left:176px;top:291px;width:170px;"></div>
  <div class="voucher-field" style="top:307px;">für:</div>
  <div class="voucher-line" style="left:176px;top:323px;width:170px;"></div>
  <div class="voucher-field" style="top:357px;">Gutscheinnummer:</div>
  <div class="voucher-line" style="left:286px;top:375px;width:169px;"></div>

  <div class="brand-tile">
    <span class="brand-mark"></span>
    <span>Jonas Keltermann</span>
    <span>Fotografie</span>
  </div>

  <div class="photo" role="img" aria-label="Porträt des Fotografen auf einem Felsen im Herbstwald" style="left:635px;top:198px;width:143px;height:201px;background:linear-gradient(180deg,#c9cfd0 0%,#8f8a6e 45%,#a77a4c 80%,#6e4a2a 100%);"></div>
  <div class="photo" role="img" aria-label="Paar kuschelt in einem Boot am Strand" style="left:786px;top:34px;width:176px;height:118px;background:linear-gradient(135deg,#d8cbb8 0%,#9fb3c0 50%,#2f3440 100%);"></div>
  <div class="photo" role="img" aria-label="Paar im hohen Gras" style="left:968px;top:34px;width:176px;height:118px;background:linear-gradient(135deg,#7f9a62 0%,#b8c09a 50%,#6e8656 100%);"></div>
  <div class="photo" role="img" aria-label="Paar sitzt auf einem Steinstrand" style="left:786px;top:158px;width:176px;height:117px;background:linear-gradient(135deg,#8c9aa0 0%,#b7aa98 50%,#d8d4cf 100%);"></div>
  <div class="photo" role="img" aria-label="Paar auf einem Waldweg im Sonnenlicht" style="left:968px;top:158px;width:176px;height:117px;background:linear-gradient(135deg,#dfe2d8 0%,#9aa06a 45%,#c9a25c 100%);"></div>
  <div class="photo" role="img" aria-label="Babybauch-Shooting eines Paares am Strand" style="left:786px;top:281px;width:176px;height:118px;background:linear-gradient(180deg,#e6e1dc 0%,#b9aea4 60%,#7f99ad 100%);"></div>
  <div class="photo" role="img" aria-label="Paar an einer mediterranen Küste" style="left:968px;top:281px;width:176px;height:118px;background:linear-gradient(180deg,#c6d4dc 0%,#5f7a4a 40%,#d9cfc2 100%);"></div>

  <div class="leaf-spray" role="img" aria-label="Zarter Zweig als Verzierung" style="left:1032px;top:322px;width:150px;height:120px;background:radial-gradient(ellipse at center, var(--leaf) 0%, rgba(216,201,168,0) 70%);"></div>
</body>
</html>
```